Extremely Professional Lawyer needs letterhead for new boutique real estate law firm

I need letterhead for my new solo practice law firm. I practiced as a partner in a huge global law firm for years. Now I am starting a solo firm where I will deliver very high-quality legal services that are real-estate focused. The idea is that my practice will be very focused but that the services will be at the quality level provided by partners at high-profile law firms. The name of my law firm will be Brenner Law Group, LLC. For now, I am the only lawyer. I expect to negotiate and draft house sale/purchase contracts and close house deals. Eventually, I would like to do small-scale development deals for developer clients, a specialty of mine.

Industry/Entity Type

Boutique

```html
<!DOCTYPE html>
<html lang="en">
<head>
<meta charset="utf-8">
<title>Brenner Law Group, LLC — Stationery</title>
<link rel="stylesheet" href="https://fonts.googleapis.com/css2?family=Marcellus&family=Didact+Gothic&display=swap">
<style>
  :root {
    --orange: #fb4b1c;
    --orange-text: #e8471c;
    --cyan: #4ef2ec;
    --blue: #4a8ff0;
    --ink: #2a2a2a;
    --paper: #ffffff;
    --backdrop: #e4e7e8;
  }
  * { margin: 0; padding: 0; box-sizing: border-box; }
  html, body { width: 1200px; height: 1000px; overflow: hidden; }
  body { background: var(--backdrop); position: relative; }

  /* Letterhead */
  .letterhead {
    position: absolute; left: 430px; top: 20px;
    width: 720px; height: 955px;
    background: var(--paper);
    box-shadow: 0 2px 10px rgba(0,0,0,.18);
  }
  .letterhead .art { position: absolute; inset: 0; }
  .letterhead .firm-name {
    position: absolute; left: 26px; top: 108px;
    font-family: "Marcellus", serif; font-size: 23px; color: var(--ink);
    display: flex; align-items: center; gap: 10px;
  }
  .mark-square { width: 14px; height: 14px; background: var(--orange); display: inline-block; }
  .offices {
    position: absolute; left: 598px; top: 62px;
    list-style: none;
    font-family: "Didact Gothic", sans-serif; font-size: 11px; line-height: 14px;
    color: var(--orange-text);
  }
  .offices li { position: relative; padding-left: 16px; margin-bottom: 6px; }
  .offices li::before {
    content: ""; position: absolute; left: 0; top: 4px;
    width: 6px; height: 6px; background: var(--cyan);
  }
  .letterhead .web {
    position: absolute; left: 6px; bottom: 22px;
    font-family: "Didact Gothic", sans-serif; font-size: 22px; color: var(--paper);
  }

  /* Business card */
  .card {
    position: absolute; left: 50px; top: 205px;
    width: 580px; height: 330px;
    background: var(--paper);
    box-shadow: 0 2px 10px rgba(0,0,0,.22);
    overflow: hidden;
  }
  .card .art { position: absolute; inset: 0; }
  .card .firm-name {
    position: absolute; left: 0; right: 0; top: 52px;
    display: flex; justify-content: center; align-items: center; gap: 10px;
    font-family: "Marcellus", serif; font-size: 22px; color: var(--ink);
  }
  .card .person {
    position: absolute; left: 28px; top: 148px;
    font-family: "Marcellus", serif; font-size: 26px; color: var(--paper);
  }
  .card .address {
    position: absolute; left: 30px; top: 196px;
    font-family: "Marcellus", serif; font-size: 18px; line-height: 23px; color: var(--paper);
    display: flex; gap: 6px;
  }
  .contacts {
    position: absolute; left: 322px; top: 194px; list-style: none;
    font-family: "Marcellus", serif; font-size: 17px; line-height: 24.5px; color: var(--paper);
  }
  .contacts li { display: flex; align-items: center; gap: 12px; }
  .contacts svg { width: 18px; height: 18px; flex: none; }
  .icon-square { width: 14px; height: 14px; margin: 0 2px; background: var(--paper); flex: none; }
</style>
</head>
<body>

<section class="letterhead" aria-label="Letterhead">
  <svg class="art" viewBox="0 0 720 955" aria-hidden="true">
    <path d="M370 10 Q560 50 592 188 Q585 80 470 10 Z" fill="var(--cyan)"/>
    <path d="M0 798 Q420 835 720 690 L720 738 Q420 870 0 842 Z" fill="var(--orange)"/>
    <path d="M0 858 Q380 885 640 790 Q460 930 330 955 L0 955 Z" fill="var(--orange)"/>
    <path d="M350 955 Q600 905 720 768 L720 800 Q650 905 470 955 Z" fill="var(--cyan)"/>
  </svg>
  <div class="firm-name"><span class="mark-square"></span>Brenner Law Group, LLC</div>
  <ul class="offices">
    <li>Elmridge, NY 10590<br>914-555-0142</li>
    <li>27 N Maple Ave<br>Pine Hollow, NY 10577<br>914-555-0187</li>
  </ul>
  <div class="web">www.BrennerLawGroup.com</div>
</section>

<section class="card" aria-label="Business card">
  <svg class="art" viewBox="0 0 580 330" aria-hidden="true">
    <path d="M0 92 L300 120 L580 108 L580 120 L300 138 L0 108 Z" fill="var(--blue)"/>
    <path d="M0 108 L300 138 L580 120 L580 330 L0 330 Z" fill="var(--orange)"/>
  </svg>
  <div class="firm-name"><span class="mark-square"></span>Brenner Law Group, LLC</div>
  <div class="person">Professor M</div>
  <div class="address">
    <svg width="16" height="20" viewBox="0 0 16 20" aria-hidden="true"><path d="M8 0a7 7 0 0 0-7 7c0 5 7 13 7 13s7-8 7-13a7 7 0 0 0-7-7Zm0 10a3 3 0 1 1 0-6 3 3 0 0 1 0 6Z" fill="var(--paper)"/></svg>
    <span>14 Harbour Lane<br>Coral Bay, NSW 2461</span>
  </div>
  <ul class="contacts">
    <li><svg viewBox="0 0 18 18" aria-hidden="true"><rect x="5" y="1" width="8" height="16" rx="1.5" fill="none" stroke="var(--paper)" stroke-width="1.5"/><rect x="7" y="4" width="4" height="5" fill="var(--paper)"/></svg>0400 555 123</li>
    <li><svg viewBox="0 0 18 18" aria-hidden="true"><rect x="1" y="4" width="16" height="11" fill="var(--paper)"/><path d="M1 4 L9 10 L17 4" fill="none" stroke="var(--orange)" stroke-width="1.3"/></svg>professorm@mailbox.com</li>
    <li><span class="icon-square"></span>@brennerlawgroup</li>
    <li><span class="icon-square"></span>www.BrennerLawGroup.com</li>
  </ul>
</section>

</body>
</html>
```